Event Poster Design for Camp for Teenagers

I need graphics designed for our summer camps event. These camps are for teenagers, 6-12th grades. Primary graphic design is for a 11x17 poster but will also need the images resized for social, 16x9 title slide, and a postcard size. Graphic should include the following:Main Title: Ridgeway Youthline Summer CampsDates: High School - June 3-7; Middle School - June 17-21; Merge - June 24 - 28Register at SDNextGen.comFor each camp, include name and headshot of speaker:High: Liam Brevik (guy in blue shirt)Middle: Marla Penhow (girl)Merge: Joey SilvaInclude Ridgeway Youthline logoBlack Hills Retreat Center, Deadwood, SDGraphic should be attractive to teenagers. Ideas - geometric shapes, 90's coloring/imagery, bright colors, soft earth tones, etc. Open to ideasMy graphic design experience is VERY limited. I will need help receiving the files I need in the various sizes. Thank you.

```html
<!DOCTYPE html>
<html lang="en">
<head>
<meta charset="utf-8">
<title>Ridgeway Youthline Summer Camps – Presentation Board</title>
<link rel="stylesheet" href="https://fonts.googleapis.com/css2?family=Open+Sans:wght@400;700&family=Titan+One&family=Kaushan+Script&display=swap">
<style>
  :root{
    --navy:#2b3990;
    --sun:#f7f08a;
    --cyan:#1fd3dd;
    --teal:#1bb3a1;
    --pink:#e0559b;
    --ink:#111111;
    --paper:#ffffff;
    --photo-dark:#5a5a5a;
    --photo-light:#c9c9c9;
  }
  html,body{margin:0;padding:0;overflow:hidden;background:var(--paper);}
  .board{position:relative;width:1200px;height:1004px;overflow:hidden;background:var(--paper);font-family:"Open Sans",sans-serif;}
  .rule{position:absolute;left:59px;width:1087px;height:4px;background:var(--navy);}
  .rule--top{top:0;}
  .rule--bottom{bottom:0;}
  .label{position:absolute;margin:0;font-size:17.5px;color:var(--navy);font-weight:400;letter-spacing:.2px;white-space:nowrap;}
  .label strong{font-weight:700;}
  .label--poster{left:66px;top:81px;}
  .label--social-event{left:623px;top:133px;}
  .label--social-full{left:623px;top:541px;}
  .artboard{position:absolute;display:block;}
  .artboard--poster{left:59px;top:137px;width:519px;height:801px;}
  .artboard--social-event{left:623px;top:194px;width:522px;height:293px;}
  .artboard--social-full{left:623px;top:597px;width:522px;height:293px;}
  .defs{position:absolute;width:0;height:0;overflow:hidden;}
  .t-brand{font-family:"Titan One",sans-serif;}
  .t-script{font-family:"Kaushan Script",cursive;}
  .t-body{font-family:"Open Sans",sans-serif;font-weight:700;}
</style>
</head>
<body>
<div class="board">
  <div class="rule rule--top"></div>

  <p class="label label--poster"><strong>RIDGEWAY YOUTHLINE</strong> | MAIN POSTER</p>
  <p class="label label--social-event"><strong>RIDGEWAY YOUTHLINE</strong> &nbsp;| SOCIAL MEDIA_ONLY THE EVENT GRAPHIC</p>
  <p class="label label--social-full"><strong>RIDGEWAY YOUTHLINE</strong> &nbsp;| SOCIAL MEDIA_ALL INFO</p>

  <svg class="defs" aria-hidden="true">
    <defs>
      <g id="title-lockup">
        <ellipse cx="140" cy="68" rx="72" ry="52" fill="var(--cyan)" role="img" aria-label="Palm tree illustration"/>
        <polygon points="54,119 531,154 271,369" fill="var(--cyan)"/>
        <polygon points="126,124 486,9 396,229" fill="var(--teal)"/>
        <g transform="translate(318,126) rotate(-14)">
          <text class="t-brand" x="2" y="3" font-size="31" text-anchor="middle" fill="var(--ink)">Ridgeway Youthline</text>
          <text class="t-brand" x="0" y="0" font-size="31" text-anchor="middle" fill="var(--paper)">Ridgeway Youthline</text>
        </g>
        <text class="t-script" transform="translate(300,212) rotate(-12)" font-size="98" text-anchor="middle" fill="var(--pink)" stroke="var(--sun)" stroke-width="8" paint-order="stroke" stroke-linejoin="round">Summer</text>
        <text class="t-script" transform="translate(392,292) rotate(-10)" font-size="98" text-anchor="middle" fill="var(--pink)" stroke="var(--sun)" stroke-width="8" paint-order="stroke" stroke-linejoin="round">Camps</text>
      </g>

      <linearGradient id="photo-tone" x1="0" y1="0" x2="1" y2="1">
        <stop offset="0" stop-color="var(--photo-light)"/>
        <stop offset="1" stop-color="var(--photo-dark)"/>
      </linearGradient>

      <g id="speaker-lineup">
        <!-- High school -->
        <polygon points="84,324 66,524 281,547" fill="url(#photo-tone)" role="img" aria-label="Headshot of speaker Liam Brevik"/>
        <g transform="translate(300,440) rotate(-15)">
          <rect x="-122" y="-66" width="262" height="46" fill="var(--cyan)"/>
          <text class="t-brand" x="-112" y="-32" font-size="27" fill="var(--ink)">HIGH SCHOOL</text>
          <rect x="-122" y="-22" width="168" height="42" fill="var(--cyan)"/>
          <text class="t-brand" x="-112" y="10" font-size="25" fill="var(--ink)">JUNE 3-7</text>
        </g>
        <g transform="translate(372,497) rotate(-10)">
          <rect x="-116" y="-21" width="232" height="40" fill="var(--paper)"/>
          <text x="-100" y="8" fill="var(--cyan)"><tspan class="t-script" font-size="19">with </tspan><tspan class="t-brand" font-size="17">LIAM BREVIK</tspan></text>
        </g>

        <!-- Middle school -->
        <circle cx="463" cy="594" r="88" fill="url(#photo-tone)" role="img" aria-label="Headshot of speaker Marla Penhow"/>
        <g transform="translate(274,614) rotate(3)">
          <rect x="-148" y="-45" width="296" height="50" fill="var(--pink)"/>
          <text class="t-brand" x="-134" y="-9" font-size="27" fill="var(--ink)">MIDDLE SCHOOL</text>
          <rect x="-34" y="3" width="180" height="42" fill="var(--pink)"/>
          <text class="t-brand" x="-16" y="35" font-size="24" fill="var(--ink)">JUNE 17 -21</text>
        </g>
        <g transform="translate(366,690) rotate(-2)">
          <rect x="-116" y="-20" width="232" height="40" fill="var(--paper)"/>
          <text x="-98" y="8" fill="var(--pink)"><tspan class="t-script" font-size="19">with </tspan><tspan class="t-brand" font-size="17">MARLA PENHOW</tspan></text>
        </g>

        <!-- Merge -->
        <polygon points="34,764 126,684 226,744 216,859 106,874" fill="url(#photo-tone)" role="img" aria-label="Photo of speaker Danny Obert"/>
        <g transform="translate(298,784) rotate(-5)">
          <rect x="-106" y="-42" width="200" height="44" fill="var(--teal)"/>
          <text class="t-brand" x="-94" y="-8" font-size="28" fill="var(--ink)">MERGE</text>
          <rect x="-96" y="2" width="202" height="40" fill="var(--teal)"/>
          <text class="t-brand" x="-84" y="32" font-size="24" fill="var(--ink)">JUNE 24 -28</text>
        </g>
        <g transform="translate(324,846) rotate(-5)">
          <rect x="-104" y="-18" width="208" height="36" fill="var(--paper)"/>
          <text x="-88" y="7" fill="var(--teal)"><tspan class="t-script" font-size="18">with </tspan><tspan class="t-brand" font-size="16">DANNY OBERT</tspan></text>
        </g>
      </g>
    </defs>
  </svg>

  <svg class="artboard artboard--poster" viewBox="0 0 648 1001" role="img" aria-label="Ridgeway Youthline Summer Camps poster">
    <rect width="648" height="1001" fill="var(--sun)"/>
    <use href="#title-lockup"/>
    <use href="#speaker-lineup"/>
    <text class="t-brand" x="538" y="812" font-size="25" text-anchor="middle" fill="var(--navy)"><tspan x="538">Ridgeway</tspan><tspan x="538" dy="28">Youthline</tspan></text>
    <polygon points="460,858 621,852 616,904 452,904" fill="var(--navy)"/>
    <text class="t-body" x="537" y="876" font-size="15" text-anchor="middle" fill="var(--paper)">Register at</text>
    <text class="t-body" x="537" y="896" font-size="14" text-anchor="middle" fill="var(--paper)">RidgewayYouthline.com</text>
    <polygon points="68,930 648,920 648,1001 68,1001" fill="var(--pink)"/>
    <text class="t-body" x="617" y="982" font-size="17" text-anchor="end" fill="var(--paper)">CEDAR FORK RETREAT CENTER | PINE HOLLOW, SD</text>
  </svg>

  <svg class="artboard artboard--social-event" viewBox="0 0 652 366" role="img" aria-label="Ridgeway Youthline Summer Camps social graphic">
    <rect width="652" height="366" fill="var(--sun)"/>
    <use href="#title-lockup" transform="translate(61,21) scale(0.745)"/>
  </svg>

  <svg class="artboard artboard--social-full" viewBox="0 0 652 366" role="img" aria-label="Ridgeway Youthline Summer Camps social graphic with camp details">
    <rect width="652" height="366" fill="var(--sun)"/>
    <use href="#title-lockup" transform="translate(6,50) scale(0.553)"/>
    <use href="#speaker-lineup" transform="translate(320,-177) scale(0.62)"/>
  </svg>

  <div class="rule rule--bottom"></div>
</div>
</body>
</html>
```